Business Card Design

We need a business card design for a Executive search firm based in London & the North East called Kestrelby. We specialise in mid - snr level (£50k - £200k) IT placements. Our company colour is navy blue.

Target Market(s)

CEO, HR Director, Sales Director/VP - (35 - 50), well educated, British, European & American

Industry/Entity Type

Business

Contact Information for Business Card

Kestrelby Staffing Limited, Owen Caskell
Mobile - 0044 7731 482 616
London Office - Kestrelby House, 27 Fernmoor, Wexcombe. HA5 3LQ
Tel: 00 44 20 418 62093
North East Office – Velmora Centre, Ashgrove Way, Tillerby, NE41 2RD
Tel: 00 44 191 6842051
www.kestrelbystaffing-example.com

Also the same details for my Business Partner Ravi Tolani
with his mobile number as 0044 7852 307718

Requirements
Must have
• must have the same logo

the logo needs to be the same but made sharper

```html
<!DOCTYPE html>
<html lang="en">
<head>
<meta charset="utf-8">
<title>Kestrelby Staffing – Business Card</title>
<link rel="stylesheet" href="https://fonts.googleapis.com/css2?family=Cinzel:wght@400;600&family=Montserrat:wght@500&family=Questrial&display=swap">
<style>
  :root {
    --page: #ececec;
    --navy: #1c2f4a;
    --navy-deep: #233a5c;
    --steel: #4a6688;
    --steel-light: #8aa0bb;
    --paper: #eef1f4;
    --ink: #1d2a3c;
    --ink-soft: #2d3f57;
    --white: #ffffff;
    --teal-dark: #0b3350;
    --teal-mid: #2a7ca6;
    --logo-grey: #dfe4e8;
  }
  * { box-sizing: border-box; margin: 0; padding: 0; }
  html, body { width: 1200px; height: 480px; overflow: hidden; }
  body { background: var(--page); position: relative; }

  .card {
    position: absolute;
    top: 74px;
    width: 540px;
    height: 340px;
    overflow: hidden;
    box-shadow: 0 4px 10px rgba(0,0,0,.25);
  }
  .card--front { left: 54px; }
  .card--back { left: 628px; }
  .card__bg { position: absolute; inset: 0; width: 100%; height: 100%; }

  /* front */
  .brand {
    position: absolute;
    font-family: "Questrial", sans-serif;
    font-weight: 400;
    color: var(--ink-soft);
    display: flex;
    align-items: center;
    gap: 8px;
  }
  .brand--front { top: 26px; left: 318px; font-size: 34px; }
  .brand__dot { width: 14px; height: 14px; border-radius: 50%; background: var(--ink-soft); }

  .website {
    position: absolute;
    top: 92px; left: 16px;
    font-family: "Montserrat", sans-serif;
    font-weight: 500;
    font-size: 13px;
    letter-spacing: .6px;
    text-transform: uppercase;
    color: var(--ink);
  }
  .holder {
    position: absolute;
    top: 120px; left: 0; width: 540px;
    text-align: center;
    font-family: "Cinzel", serif;
    font-weight: 400;
    font-size: 27px;
    letter-spacing: 1px;
    color: var(--white);
    padding-right: 60px;
  }
  .mobile {
    position: absolute;
    top: 196px; left: 62px;
    font-family: "Montserrat", sans-serif;
    font-weight: 500;
    font-size: 21px;
    color: var(--ink);
  }
  .office {
    position: absolute;
    font-family: "Cinzel", serif;
    font-size: 13px;
    line-height: 18px;
  }
  .office--london { top: 230px; left: 18px; color: var(--white); }
  .office--north { top: 230px; right: 16px; text-align: right; color: var(--ink); }
  .tel {
    position: absolute;
    top: 285px;
    font-family: "Montserrat", sans-serif;
    font-weight: 500;
    font-size: 18px;
  }
  .tel--london { left: 54px; color: var(--white); }
  .tel--north { left: 354px; color: var(--ink); }

  /* back */
  .brand--back {
    top: 132px; left: 50px;
    font-size: 64px;
    color: var(--logo-grey);
    gap: 16px;
  }
  .brand--back .brand__dot { width: 26px; height: 26px; background: var(--logo-grey); }
</style>
</head>
<body>

<section class="card card--front" aria-label="Business card front">
  <svg class="card__bg" viewBox="0 0 540 340" aria-hidden="true">
    <defs>
      <linearGradient id="front-top" x1="0" y1="0" x2="0" y2="1">
        <stop offset="0" stop-color="#f6f8fa"/>
        <stop offset="1" stop-color="#c9d2dd"/>
      </linearGradient>
      <linearGradient id="front-lower" x1="0" y1="0" x2="1" y2="1">
        <stop offset="0" stop-color="#7e95b2"/>
        <stop offset="1" stop-color="#3d5a7c"/>
      </linearGradient>
      <linearGradient id="name-band" x1="0" y1="0" x2="0" y2="1">
        <stop offset="0" stop-color="#8aa0bb"/>
        <stop offset=".35" stop-color="#3f5b80"/>
        <stop offset="1" stop-color="#1f3556"/>
      </linearGradient>
      <linearGradient id="paper-wedge" x1="0" y1="0" x2="1" y2="1">
        <stop offset="0" stop-color="#f3f5f7"/>
        <stop offset="1" stop-color="#d9dee4"/>
      </linearGradient>
      <radialGradient id="icon-blue" cx=".4" cy=".35" r=".7">
        <stop offset="0" stop-color="#bfe9ff"/>
        <stop offset="1" stop-color="#1c7fc0"/>
      </radialGradient>
    </defs>
    <rect class="top-panel" width="540" height="180" fill="url(#front-top)"/>
    <circle cx="300" cy="40" r="58" fill="none" stroke="#ffffff" stroke-opacity=".7" stroke-width="6"/>
    <circle cx="300" cy="40" r="40" fill="none" stroke="#b7c2cf" stroke-opacity=".6" stroke-width="2"/>
    <rect class="lower-panel" y="176" width="540" height="164" fill="url(#front-lower)"/>
    <polygon class="paper-wedge" points="282,178 540,178 540,340 372,340" fill="url(#paper-wedge)"/>
    <circle cx="330" cy="300" r="74" fill="none" stroke="#ffffff" stroke-opacity=".35" stroke-width="5"/>
    <circle cx="330" cy="300" r="54" fill="none" stroke="#ffffff" stroke-opacity=".25" stroke-width="2"/>
    <rect class="name-band" y="110" width="540" height="62" fill="url(#name-band)"/>
    <rect class="name-strip" x="210" y="166" width="340" height="16" rx="8" fill="#1c2f4a"/>
    <rect class="web-pill" x="-20" y="86" width="372" height="24" rx="12" fill="#ffffff"/>
    <g class="icon-phone" transform="translate(16,192)" fill="#1d2a3c">
      <path d="M6 2 h8 l3 8 -4 3 c2 5 5 8 10 10 l3 -4 8 3 v8 c0 2 -2 3 -4 3 C15 33 3 21 2 6 c0 -2 2 -4 4 -4z"/>
      <rect x="0" y="30" width="38" height="3" rx="1.5"/>
    </g>
    <g class="icon-tel">
      <circle cx="32" cy="298" r="11" fill="url(#icon-blue)" stroke="#ffffff" stroke-width="2"/>
      <circle cx="32" cy="298" r="5" fill="none" stroke="#ffffff" stroke-width="1.5"/>
      <circle cx="332" cy="298" r="11" fill="url(#icon-blue)" stroke="#ffffff" stroke-width="2"/>
      <circle cx="332" cy="298" r="5" fill="none" stroke="#ffffff" stroke-width="1.5"/>
    </g>
  </svg>

  <div class="brand brand--front">Kestrelby<span class="brand__dot"></span></div>
  <p class="website">www.kestrelbystaffing-example.com</p>
  <h1 class="holder">Owen Caskell</h1>
  <p class="mobile">0044 7731 482 616</p>
  <address class="office office--london">London Office<br>Kestrelby House,<br>27 Fernmoor, Wexcombe. HA5 3LQ</address>
  <p class="tel tel--london">00 44 20 418 62093</p>
  <address class="office office--north">North East Office<br>Velmora Centre, Ashgrove Way<br>Tillerby, NE41 2RD</address>
  <p class="tel tel--north">00 44 191 6842051</p>
</section>

<section class="card card--back" aria-label="Business card back">
  <svg class="card__bg" viewBox="0 0 540 340" aria-hidden="true">
    <defs>
      <linearGradient id="back-fill" x1="0" y1="0" x2="0" y2="1">
        <stop offset="0" stop-color="#0b3350"/>
        <stop offset=".42" stop-color="#1e6a92"/>
        <stop offset=".55" stop-color="#3a93bd"/>
        <stop offset=".7" stop-color="#1a5b80"/>
        <stop offset="1" stop-color="#0c3452"/>
      </linearGradient>
      <radialGradient id="back-glow" cx=".55" cy=".5" r=".5">
        <stop offset="0" stop-color="#8fd2f0" stop-opacity=".45"/>
        <stop offset="1" stop-color="#8fd2f0" stop-opacity="0"/>
      </radialGradient>
    </defs>
    <rect width="540" height="340" fill="url(#back-fill)"/>
    <rect width="540" height="340" fill="url(#back-glow)"/>
    <g class="rings" fill="none" stroke="#9fd6f2">
      <circle cx="40" cy="20" r="70" stroke-opacity=".35" stroke-width="3"/>
      <circle cx="150" cy="210" r="100" stroke-opacity=".3" stroke-width="2"/>
      <circle cx="150" cy="210" r="118" stroke-opacity=".2" stroke-width="6"/>
      <circle cx="470" cy="200" r="150" stroke-opacity=".25" stroke-width="2"/>
      <circle cx="470" cy="200" r="120" stroke-opacity=".2" stroke-width="1.5"/>
    </g>
  </svg>
  <div class="brand brand--back">Kestrelby<span class="brand__dot"></span></div>
</section>

</body>
</html>
```